Velborne Systems needs a business card

The logo we have uploaded is going to be the image centered on the back.
The business card color is going to be black. Increase the contrast in the logo and lettering so the grey stands out from the black and is more readable. Keep the shadow effect if you can.
On the front, the only part of the logo that should be used is the Egyptian character. We would like the following information included: Name (first last), Title, Phone number, email and company name (Velborne Systems).
The images of colored sound waves we uploaded is a concept we would like implemented on the front as well but please do not use the exact image. It is for guideline purposes.
Get creative with the empty space. We are a technology company that deals with sound and lights. Please not too busy.
Thank you, we look forward to all your submissions.

```html
<!DOCTYPE html>
<html lang="en">
<head>
<meta charset="utf-8">
<title>Velborne Systems – Business Card</title>
<link href="https://fonts.googleapis.com/css2?family=Quicksand:wght@500&family=Tinos&display=swap" rel="stylesheet">
<style>
  :root {
    --page-bg: #e9e6e1;
    --card-white: #ffffff;
    --card-black: #1b1b1c;
    --accent-red: #e4222b;
    --ink-grey: #3a3a3c;
    --soft-grey: #8d8d90;
  }
  * { margin: 0; padding: 0; box-sizing: border-box; }
  html, body { width: 1200px; height: 892px; overflow: hidden; }
  body {
    background: var(--page-bg);
    position: relative;
    font-family: "Tinos", "Times New Roman", serif;
  }
  .card {
    position: absolute;
    top: 291px;
    width: 540px;
    height: 309px;
    overflow: hidden;
    box-shadow: 0 6px 18px rgba(0,0,0,0.18);
  }
  .card-front { left: 40px; background: var(--card-white); }
  .card-back  { left: 620px; background: var(--card-white); }

  /* front */
  .front-arc { position: absolute; inset: 0; }
  .front-brand {
    position: absolute;
    left: 40px;
    top: 132px;
    width: 190px;
    text-align: center;
    font-family: "Tinos", "Times New Roman", serif;
    font-size: 24px;
    line-height: 1.15;
    color: var(--ink-grey);
  }
  .holder { position: absolute; left: 290px; top: 72px; }
  .holder-name {
    font-size: 30px;
    letter-spacing: 1px;
    color: var(--accent-red);
    text-transform: uppercase;
    line-height: 1;
  }
  .holder-title {
    font-size: 17px;
    color: var(--ink-grey);
    margin-top: 2px;
  }
  .contact-list { position: absolute; left: 280px; top: 168px; list-style: none; }
  .contact-item {
    display: flex;
    align-items: flex-start;
    gap: 12px;
    font-size: 15px;
    color: var(--ink-grey);
    line-height: 1.2;
    margin-bottom: 11px;
  }
  .contact-icon { flex: 0 0 18px; width: 18px; height: 18px; margin-top: -1px; }

  /* back */
  .back-band {
    position: absolute;
    left: 0; right: 0;
    top: 64px;
    height: 180px;
    background: var(--card-black);
    display: flex;
    align-items: center;
    justify-content: center;
    gap: 14px;
  }
  .back-mark {
    width: 16px; height: 16px;
    background: var(--accent-red);
  }
  .back-wordmark {
    font-family: "Quicksand", sans-serif;
    font-weight: 500;
    font-size: 26px;
    letter-spacing: 3px;
    text-transform: uppercase;
    color: var(--accent-red);
    text-shadow: none;
  }
</style>
</head>
<body>
  <section class="card card-front" aria-label="Business card front">
    <svg class="front-arc" width="540" height="309" viewBox="0 0 540 309" aria-hidden="true">
      <circle cx="92" cy="150" r="176" fill="none" stroke="var(--accent-red)" stroke-width="4"/>
    </svg>
    <p class="front-brand">Velborne Systems</p>
    <div class="holder">
      <h1 class="holder-name">Marcus Hale</h1>
      <p class="holder-title">Maneging Directer</p>
    </div>
    <ul class="contact-list">
      <li class="contact-item">
        <svg class="contact-icon" viewBox="0 0 18 18" aria-hidden="true"><circle cx="9" cy="9" r="8" fill="none" stroke="var(--accent-red)" stroke-width="1.2"/><path d="M6 5.5l1.6-.5 1 2-1 .8a5 5 0 0 0 2.6 2.6l.8-1 2 1-.5 1.6c-3.6 0-6.5-2.9-6.5-6.5z" fill="var(--accent-red)"/></svg>
        <span>+1 555 018 2247</span>
      </li>
      <li class="contact-item">
        <svg class="contact-icon" viewBox="0 0 18 18" aria-hidden="true"><circle cx="9" cy="9" r="8" fill="none" stroke="var(--accent-red)" stroke-width="1.2"/><rect x="4.8" y="6" width="8.4" height="6" fill="none" stroke="var(--accent-red)" stroke-width="1.1"/><path d="M4.8 6l4.2 3.4L13.2 6" fill="none" stroke="var(--accent-red)" stroke-width="1.1"/></svg>
        <span>info@velborne-mail.com</span>
      </li>
      <li class="contact-item">
        <svg class="contact-icon" viewBox="0 0 18 18" aria-hidden="true"><circle cx="9" cy="9" r="8" fill="none" stroke="var(--accent-red)" stroke-width="1.2"/><path d="M9 13.5s-3.2-3.3-3.2-5.6a3.2 3.2 0 0 1 6.4 0c0 2.3-3.2 5.6-3.2 5.6z" fill="var(--accent-red)"/><circle cx="9" cy="7.9" r="1.1" fill="#fff"/></svg>
        <span>42 Calloway Avenue<br>Denver 80210, United States</span>
      </li>
    </ul>
  </section>

  <section class="card card-back" aria-label="Business card back">
    <div class="back-band">
      <span class="back-mark" aria-hidden="true"></span>
      <span class="back-wordmark">Velborne Systems</span>
    </div>
  </section>
</body>
</html>
```